brindlewood carpentry business card 2.0

id like to get some extra info added to my current business card ,but i am also open to a new design as well ,id like it to be a clean professional look
i have attached the original card files, i have also attached the ridgemark guild logo and licensed builder logo that id like to add to all the current info on the old card
also the color green is important as seen in the company logo

Industry/Entity Type

Carpentry

Colors
9bcb3c

```html
<!DOCTYPE html>
<html lang="en">
<head>
<meta charset="utf-8">
<title>Brindlewood Carpentry – Business Card</title>
<link rel="stylesheet" href="https://fonts.googleapis.com/css2?family=Questrial&display=swap">
<style>
  :root {
    --brand-green: #9bcb3c;
    --pale-green: #f5f8ee;
    --ink: #1d1d1b;
    --white: #ffffff;
    --card-edge: #9a9a9a;
    --guild-blue: #1f4f8f;
    --badge-grey: #e6e9e1;
    --badge-ring: #a9c64c;
  }
  * { margin: 0; padding: 0; box-sizing: border-box; }
  html, body {
    width: 1200px;
    height: 720px;
    overflow: hidden;
    background: var(--white);
  }
  .canvas {
    position: relative;
    width: 1200px;
    height: 720px;
    overflow: hidden;
    background: var(--white);
    font-family: "Questrial", sans-serif;
  }
  .card {
    position: absolute;
    left: 40px;
    top: 40px;
    width: 1120px;
    height: 640px;
    overflow: hidden;
    border: 1px solid var(--card-edge);
    background: var(--white);
  }
  .card-shapes {
    position: absolute;
    inset: 0;
  }
  .holder-name {
    position: absolute;
    left: 0;
    width: 600px;
    top: 178px;
    text-align center;
    text-align: center;
    color: var(--white);
    font-size: 48px;
    font-weight: 400;
    line-height: 1;
  }
  .holder-role {
    position: absolute;
    left: 98px;
    top: 246px;
    color: var(--white);
    font-size: 24px;
    font-weight: 400;
    letter-spacing: 0.3px;
  }
  .divider {
    position: absolute;
    left: 40px;
    top: 295px;
    width: 570px;
    height: 8px;
  }
  .contact-list {
    position: absolute;
    left: 96px;
    top: 325px;
    list-style: none;
  }
  .contact-item {
    display: flex;
    align-items: center;
    height: 42px;
    color: var(--white);
    font-size: 26px;
    letter-spacing: 0.3px;
  }
  .contact-icon {
    width: 38px;
    height: 34px;
    margin-right: 33px;
    flex: none;
  }
  .brand-name {
    position: absolute;
    right: 74px;
    top: 66px;
    text-align: right;
    color: var(--ink);
    font-weight: 400;
    letter-spacing: 2px;
  }
  .brand-name-main {
    display: block;
    font-size: 56px;
    line-height: 1.1;
  }
  .brand-name-sub {
    display: block;
    font-size: 36px;
    line-height: 1.3;
    margin-top: 12px;
  }
  .badge-guild {
    position: absolute;
    left: 810px;
    top: 243px;
    width: 81px;
    height: 96px;
    background: var(--guild-blue);
  }
  .badge-certificate {
    position: absolute;
    left: 928px;
    top: 239px;
    width: 94px;
    height: 94px;
    border-radius: 50%;
    background: var(--badge-grey);
    border: 4px solid var(--badge-ring);
  }
</style>
</head>
<body>
<main class="canvas">
  <section class="card">
    <svg class="card-shapes" width="1120" height="640" viewBox="0 0 1120 640" aria-hidden="true">
      <circle cx="845" cy="320" r="320" fill="var(--pale-green)"/>
      <rect x="0" y="0" width="320" height="640" fill="var(--brand-green)"/>
      <circle cx="320" cy="320" r="320" fill="var(--brand-green)"/>
    </svg>

    <h1 class="holder-name">Daniel Marsh</h1>
    <p class="holder-role">director BrindleWood Carpentry Ltd</p>

    <svg class="divider" viewBox="0 0 570 8" preserveAspectRatio="none" aria-hidden="true">
      <path d="M0 5 Q 40 2.5 120 3 L 560 1 Q 570 3 566 5.5 L 130 7 Q 60 7.5 0 5 Z" fill="var(--white)"/>
    </svg>

    <ul class="contact-list">
      <li class="contact-item">
        <svg class="contact-icon" viewBox="0 0 38 34" aria-hidden="true">
          <path d="M8 2 L14 2 L16 10 L12 13 Q15 20 21 23 L24 19 L31 21 L31 27 Q29 31 24 30 Q8 25 5 8 Q5 3 8 2 Z" fill="var(--white)"/>
        </svg>
        <span>02109458316</span>
      </li>
      <li class="contact-item">
        <svg class="contact-icon" viewBox="0 0 38 34" aria-hidden="true">
          <rect x="2" y="7" width="34" height="21" fill="none" stroke="var(--white)" stroke-width="3"/>
          <path d="M2 7 L19 20 L36 7" fill="none" stroke="var(--white)" stroke-width="3"/>
        </svg>
        <span>dan@brindlewoodcarpentry.co.nz</span>
      </li>
      <li class="contact-item">
        <svg class="contact-icon" viewBox="0 0 38 34" aria-hidden="true">
          <g fill="none" stroke="var(--white)" stroke-width="2.6">
            <circle cx="17" cy="18" r="14"/>
            <ellipse cx="17" cy="18" rx="6" ry="14"/>
            <line x1="3" y1="18" x2="31" y2="18"/>
            <path d="M5 11 H29 M5 25 H29"/>
          </g>
        </svg>
        <span>www.brindlewoodcarpentry.co.nz</span>
      </li>
    </ul>

    <p class="brand-name">
      <span class="brand-name-main">BRINDLEWOOD</span>
      <span class="brand-name-sub">CARPENTRY</span>
    </p>

    <div class="badge-guild" role="img" aria-label="Ridgemark Guild member badge"></div>
    <div class="badge-certificate" role="img" aria-label="Trade certification badge"></div>
  </section>
</main>
</body>
</html>
```